Valdoro Global Journeys Facebook Page

I would like to have a very professional and unique Facebook page for my business
www.valdoroglobaljourneys.com

```html
<!DOCTYPE html>
<html lang="en">
<head>
<meta charset="utf-8">
<title>Valdoro Global Journeys – Facebook Cover</title>
<link rel="stylesheet" href="https://fonts.googleapis.com/css2?family=Cabin:wght@400;600&display=swap">
<style>
  :root {
    --page-bg: #ffffff;
    --teal-deep: #1f8f98;
    --teal: #2ea3ab;
    --teal-light: #39b3ba;
    --mist-light: #f2f2f2;
    --mist-mid: #d6d6d6;
    --sky-deep: #3a66a8;
    --sky-light: #c9d8ea;
    --snow: #eef2f7;
    --rock: #4a5e7a;
    --earth: #8a5a3a;
    --text-light: #ffffff;
  }
  html, body {
    margin: 0;
    padding: 0;
    width: 1200px;
    height: 1200px;
    overflow: hidden;
    background: var(--page-bg);
  }
  .canvas {
    position: relative;
    width: 1200px;
    height: 1200px;
  }
  .cover {
    position: absolute;
    left: 30px;
    top: 389px;
    width: 1140px;
    height: 422px;
    overflow: hidden;
    font-family: "Cabin", sans-serif;
  }
  .cover-art {
    position: absolute;
    inset: 0;
    display: block;
  }
  .brand {
    position: absolute;
    left: 24px;
    top: 22px;
    display: flex;
    align-items: center;
    gap: 10px;
  }
  .brand-dot {
    width: 54px;
    height: 54px;
    border-radius: 50%;
    background: var(--teal-deep);
  }
  .brand-name {
    font-size: 24px;
    font-weight: 600;
    color: var(--teal-deep);
    letter-spacing: 0.3px;
  }
  .message {
    position: absolute;
    left: 560px;
    width: 560px;
    margin: 0;
    text-align: center;
    color: var(--text-light);
  }
  .headline {
    top: 172px;
    font-size: 50px;
    font-weight: 600;
    line-height: 1.1;
  }
  .tagline {
    top: 230px;
    font-size: 48px;
    font-weight: 400;
    line-height: 1.1;
  }
  .web-address {
    top: 374px;
    left: 605px;
    width: 520px;
    font-size: 22px;
    font-weight: 400;
    line-height: 1.2;
    letter-spacing: -0.2px;
  }
</style>
</head>
<body>
<main class="canvas">
  <section class="cover">
    <svg class="cover-art" viewBox="0 0 1140 422" width="1140" height="422">
      <defs>
        <linearGradient id="mist-photo" x1="0" y1="0" x2="0.4" y2="1">
          <stop offset="0" stop-color="var(--mist-light)"/>
          <stop offset="0.55" stop-color="var(--mist-mid)"/>
          <stop offset="1" stop-color="var(--mist-light)"/>
        </linearGradient>
        <linearGradient id="peak-photo" x1="0" y1="0" x2="0" y2="1">
          <stop offset="0" stop-color="var(--sky-deep)"/>
          <stop offset="0.35" stop-color="var(--sky-light)"/>
          <stop offset="0.6" stop-color="var(--snow)"/>
          <stop offset="0.8" stop-color="var(--rock)"/>
          <stop offset="1" stop-color="var(--earth)"/>
        </linearGradient>
        <linearGradient id="teal-panel" x1="0" y1="0" x2="1" y2="1">
          <stop offset="0" stop-color="var(--teal-deep)"/>
          <stop offset="0.5" stop-color="var(--teal)"/>
          <stop offset="1" stop-color="var(--teal-light)"/>
        </linearGradient>
      </defs>
      <rect class="mist-backdrop" x="0" y="0" width="1140" height="422" fill="url(#mist-photo)"
            role="img" aria-label="Faded grey photo of snowy Himalayan peaks"/>
      <circle class="peak-window" cx="641" cy="278" r="422" fill="url(#peak-photo)"
              role="img" aria-label="Photo of a snow-covered Himalayan summit under a blue sky"/>
      <circle class="teal-panel" cx="961" cy="299" r="438" fill="url(#teal-panel)"/>
    </svg>

    <div class="brand">
      <span class="brand-dot"></span>
      <span class="brand-name">Valdoro Global Journeys</span>
    </div>

    <h1 class="message headline">Visit the Top of the World</h1>
    <p class="message tagline">Challenge Yourself</p>
    <p class="message web-address">www.valdoroglobaljourneys.com</p>
  </section>
</main>
</body>
</html>
```